Tending the Hidden Garden; A Map Toward Calm, Purpose & Belonging

I need a book cover, for the above book title. This is a journey of the heart to know the heart of God. I think on the text, Simple (see below graphic)
Black Lettering for Tending.....Garden
Gold lettering for God
Either gold or black for the subtitle; A Map Toward Calm, Purpose, & Belonging
I would like the below graphic idea only no photograph of a person,
and White background instead of black
Simple Font, like below graphic, but open to suggestions

not age specific, Every person has been given a heart to know God, we are taking the mystery out the process to understand God is Father, loving gracious, ever present, etc. If we know His heart, we realize He's not at a distance, He is there, an ever present help

Security

• Title: Tending the Hidden Garden; A Map Toward Calm, Purpose, & Belonging
• My name, Rob Fenwick
• See Below Graphic

```html
<!DOCTYPE html>
<html lang="en">
<head>
<meta charset="utf-8">
<title>Tending the Hidden Garden — Book Cover</title>
<link rel="stylesheet" href="https://fonts.googleapis.com/css2?family=Oswald:wght@500;600;700&family=Jost:wght@600&display=swap">
<style>
  :root {
    --page: #ffffff;
    --paper-top: #fcfcfa;
    --paper-bottom: #f1f0eb;
    --ink: #0c0c0c;
    --gold: #d4bb3c;
  }
  html, body {
    margin: 0;
    width: 1200px;
    height: 1200px;
    overflow: hidden;
    background: var(--page);
  }
  .cover {
    position: absolute;
    left: 244px;
    top: 66px;
    width: 712px;
    height: 1068px;
    display: block;
  }
  .title-word {
    font-family: "Oswald", "Arial Narrow", sans-serif;
    fill: var(--ink);
  }
  .title-top { font-weight: 700; }
  .title-bottom { font-weight: 500; }
  .title-feature {
    font-family: "Oswald", "Arial Narrow", sans-serif;
    font-weight: 600;
    fill: var(--gold);
  }
  .subtitle, .author {
    font-family: "Jost", "Futura", sans-serif;
    font-weight: 600;
    fill: var(--ink);
  }
  .subtitle { font-size: 25px; letter-spacing: 4.5px; }
  .author { font-size: 48px; letter-spacing: 9px; }
</style>
</head>
<body>
<svg class="cover" viewBox="0 0 712 1068" role="img" aria-label="Book cover: Tending the Hidden Garden by Rob Fenwick">
  <defs>
    <linearGradient id="paper" x1="0" y1="0" x2="0.3" y2="1">
      <stop offset="0" stop-color="var(--paper-top)"/>
      <stop offset="1" stop-color="var(--paper-bottom)"/>
    </linearGradient>
  </defs>
  <rect class="cover-paper" width="712" height="1068" fill="url(#paper)"/>

  <text class="title-word title-top" x="356" y="236" font-size="192" text-anchor="middle" textLength="605" lengthAdjust="spacingAndGlyphs">TENDING</text>

  <text class="subtitle" x="356" y="315" text-anchor="middle">A MAP TOWARD CALM,</text>
  <text class="subtitle" x="356" y="355" text-anchor="middle">PURPOSE, &amp; BELONGING</text>

  <text class="title-feature" x="356" y="518" font-size="114" text-anchor="middle" textLength="230" lengthAdjust="spacingAndGlyphs">THE</text>
  <text class="title-feature" x="356" y="700" font-size="215" text-anchor="middle" textLength="540" lengthAdjust="spacingAndGlyphs">HIDDEN</text>

  <text class="author" x="356" y="824" text-anchor="middle" textLength="428" lengthAdjust="spacing">ROB FENWICK</text>

  <text class="title-word title-bottom" x="356" y="992" font-size="116" text-anchor="middle" textLength="560" lengthAdjust="spacing">GARDEN</text>
</svg>
</body>
</html>
```